Business Card Design Project

I need the following:

Logo -
Name - Dale Whitcomb
Title - Customer Experience Officer
Web - www.brvq.net
Phone - 555-418-3076
Updates

Project Deadline Extended
Reason: I launched the project later than anticipated. I look forward to seeing your designs. Dale

Industry/Entity Type

Business

```html
<!DOCTYPE html>
<html lang="en">
<head>
<meta charset="utf-8">
<title>Bravique Telecom Consulting — Business Card</title>
<link rel="stylesheet" href="https://fonts.googleapis.com/css2?family=Open+Sans:wght@300;400;600;800&display=swap">
<style>
  :root {
    --backdrop: #e4e4e4;
    --card: #ffffff;
    --ink: #1c1c1c;
    --ink-soft: #555555;
    --brand-blue: #2f9fe0;
    --brand-globe: #2a5fb0;
    --divider: #e2e2e2;
  }
  * { box-sizing: border-box; margin: 0; padding: 0; }
  html, body {
    width: 1200px;
    height: 944px;
    overflow: hidden;
    background: var(--backdrop);
    font-family: "Open Sans", Arial, sans-serif;
  }
  .card-sheet {
    position: absolute;
    inset: 0;
    display: flex;
    align-items: center;
    justify-content: center;
    gap: 40px;
  }
  .card {
    width: 540px;
    height: 309px;
    background: var(--card);
    box-shadow: 0 2px 10px rgba(0,0,0,0.12);
    position: relative;
  }

  /* Front */
  .card-front {
    display: flex;
    align-items: center;
    justify-content: center;
    gap: 22px;
  }
  .brand-mark {
    width: 92px;
    height: 92px;
    border-radius: 50%;
    background: var(--brand-globe);
    flex: none;
  }
  .brand-block { display: flex; flex-direction: column; }
  .brand-name {
    font-weight: 800;
    color: var(--ink);
    text-transform: uppercase;
    font-size: 25px;
    line-height: 1.02;
    letter-spacing: 0.5px;
  }
  .brand-rule {
    height: 2px;
    background: var(--brand-blue);
    margin-top: 8px;
  }
  .brand-web {
    font-weight: 800;
    color: var(--brand-blue);
    font-size: 13px;
    text-align: center;
    margin-top: 3px;
  }

  /* Back */
  .card-back { display: flex; }
  .back-brand {
    width: 50%;
    display: flex;
    flex-direction: column;
    align-items: center;
    justify-content: center;
    gap: 12px;
  }
  .back-brand .brand-mark { width: 60px; height: 60px; }
  .back-brand .brand-name { font-size: 16px; }
  .back-brand .brand-rule { margin-top: 5px; }
  .back-brand .brand-web { font-size: 10px; }
  .back-divider {
    width: 1px;
    background: var(--divider);
    margin: 40px 0;
  }
  .back-contact {
    flex: 1;
    display: flex;
    flex-direction: column;
    justify-content: center;
    padding-left: 34px;
  }
  .person-name {
    font-weight: 600;
    color: var(--brand-blue);
    font-size: 19px;
  }
  .person-title {
    font-weight: 300;
    color: var(--ink-soft);
    font-size: 12px;
    margin-top: 2px;
  }
  .phone-line {
    display: flex;
    align-items: center;
    gap: 9px;
    margin-top: 16px;
    color: var(--ink);
    font-size: 15px;
  }
  .phone-icon { width: 14px; height: 14px; fill: var(--brand-blue); }
</style>
</head>
<body>
<main class="card-sheet">
  <section class="card card-front" aria-label="Card front">
    <div class="brand-mark"></div>
    <div class="brand-block">
      <p class="brand-name">Bravique<br>Telecom<br>Consulting</p>
      <div class="brand-rule"></div>
      <p class="brand-web">www.brvq.net</p>
    </div>
  </section>

  <section class="card card-back" aria-label="Card back">
    <div class="back-brand">
      <div class="brand-mark"></div>
      <div class="brand-block">
        <p class="brand-name">Bravique<br>Telecom<br>Consulting</p>
        <div class="brand-rule"></div>
        <p class="brand-web">www.brvq.net</p>
      </div>
    </div>
    <div class="back-divider"></div>
    <div class="back-contact">
      <p class="person-name">Dale Whitcomb</p>
      <p class="person-title">Customer Experience Officer</p>
      <p class="phone-line">
        <svg class="phone-icon" viewBox="0 0 24 24" aria-hidden="true">
          <path d="M6.6 10.8a15.1 15.1 0 0 0 6.6 6.6l2.2-2.2c.3-.3.7-.4 1-.2 1.1.4 2.3.6 3.6.6.6 0 1 .4 1 1V20c0 .6-.4 1-1 1A17 17 0 0 1 3 4c0-.6.4-1 1-1h3.5c.6 0 1 .4 1 1 0 1.3.2 2.5.6 3.6.1.3 0 .7-.2 1z"/>
        </svg>
        555-418-3076
      </p>
    </div>
  </section>
</main>
</body>
</html>
```